bottle label design for a cultured milk based product

(Edit : name of the company is Qeshari . The bottle will be see through )
Edit 2 :I noticed people only sending a logo this isn't what I want please read the description

I'm starting a small dairy company for cultured milk products .

1. I need a logo
2.i need a design for the bottle label
3. I need a design for the bottle it's self

As a professional suggest for me the sizes for large medium and small (ie 1.5 liter) .

We are still brainstorming this but hope you can help us how it will be designed

The main theme behind it is as follows
Camel based milk
Cultured/fermented/probiotic milk
Fenugreek added to enhance flavour
Organic
Plant based biodegradable bottle (eco-friendly)
(Shake before use)

This must be a full label which also includes the nutritional break down table but keep it empty for us to fill in

Since on the bigger bottles has more space and I thought we could add a small story since cultured milk is part of our history (united Arab Emirates)

The idea of how the label would look like is that it can have a small outline of a camel and a brown background of sand dunes and the font would be in white but you can ignore all of this and show us what you can think of

If we have missed something , as a professional guide us .

```html
<!DOCTYPE html>
<html lang="en">
<head>
<meta charset="utf-8">
<title>Qeshari Camel Laban – Bottle Label</title>
<link href="https://fonts.googleapis.com/css2?family=Fira+Sans:wght@300;400;500;600;700&display=swap" rel="stylesheet">
<style>
  :root {
    --backdrop: #ececec;
    --label: #fbfaf8;
    --brown: #8a6e4f;
    --brown-soft: #a89178;
    --ink: #6f5a43;
    --rule: #8a6e4f;
  }
  * { box-sizing: border-box; margin: 0; padding: 0; }
  html, body {
    width: 1200px; height: 900px; overflow: hidden;
    background: var(--backdrop);
    font-family: "Fira Sans", sans-serif;
    color: var(--brown);
  }
  .stage {
    width: 1200px; height: 900px;
    display: flex; justify-content: center; align-items: center; gap: 90px;
  }
  .label {
    width: 380px; height: 600px;
    background: var(--label);
    border-radius: 18px;
    box-shadow: 0 2px 14px rgba(0,0,0,0.06);
    position: relative;
  }

  /* Front face */
  .front .brand {
    position: absolute; top: 150px; right: 34px;
    font-size: 15px; font-weight: 600; letter-spacing: 0.2px;
    display: flex; align-items: center; gap: 6px;
  }
  .front .brand .dot { width: 8px; height: 8px; border-radius: 50%; background: var(--brown); }
  .front .mascot {
    position: absolute; top: 186px; right: 52px;
    width: 48px; height: 46px; border-radius: 10px;
    background: linear-gradient(180deg, #e3d8ca, #cdbda8);
  }
  .front .title-block {
    position: absolute; top: 262px; right: 34px; text-align: right;
  }
  .front .title-kicker { font-size: 26px; font-weight: 600; line-height: 1; }
  .front .title { font-size: 92px; font-weight: 600; line-height: 0.9; letter-spacing: -1px; }
  .front .subtitle { font-size: 15.5px; font-weight: 700; letter-spacing: 0.3px; margin-top: 4px; }
  .front .note { font-size: 8px; font-weight: 500; letter-spacing: 0.4px; margin-top: 2px; }
  .front .category {
    font-size: 19px; font-weight: 300; letter-spacing: 1.6px;
    color: var(--brown-soft); margin-top: 20px;
  }
  .front .volume {
    position: absolute; bottom: 74px; right: 34px;
    font-size: 15px; font-weight: 600;
  }
  .front .fine {
    position: absolute; bottom: 46px; right: 34px; text-align: right;
    font-size: 7px; font-weight: 500; line-height: 1.3; color: var(--ink);
  }

  /* Back face */
  .back .brand {
    position: absolute; top: 176px; left: 0; right: 0; text-align: center;
  }
  .back .brand-name {
    font-size: 22px; font-weight: 600;
    display: inline-flex; align-items: center; gap: 7px;
  }
  .back .brand-name .dot { width: 9px; height: 9px; border-radius: 50%; background: var(--brown); }
  .back .brand-line {
    font-size: 10px; font-weight: 400; letter-spacing: 3px; color: var(--brown-soft);
  }
  .back .story {
    position: absolute; top: 232px; left: 52px; right: 52px;
    text-align: center; font-size: 9.2px; line-height: 1.75; color: var(--ink);
  }
  .nutrition {
    position: absolute; top: 404px; left: 40px; right: 40px;
    border: 1px solid var(--rule);
    display: grid; grid-template-columns: 78px 1fr 96px;
    height: 56px; color: var(--ink);
  }
  .nutrition .head { padding: 3px 5px; border-right: 1px solid var(--rule); }
  .nutrition .head h3 { font-size: 12px; font-weight: 700; line-height: 1; color: var(--brown); }
  .nutrition .head .cal { font-size: 7px; margin-top: 3px; display: flex; justify-content: space-between; align-items: baseline; }
  .nutrition .head .cal b { font-size: 13px; color: var(--brown); }
  .nutrition .rows { padding: 3px 5px; border-right: 1px solid var(--rule); }
  .nutrition .row {
    font-size: 6.5px; display: flex; justify-content: space-between;
    border-bottom: 0.5px solid var(--rule); padding: 1.5px 0;
  }
  .nutrition .row:last-child { border-bottom: none; }
  .nutrition .side { padding: 4px 5px; font-size: 6px; line-height: 1.35; }
  .back .fine {
    position: absolute; top: 468px; left: 40px; right: 40px;
    font-size: 6.5px; line-height: 1.4; color: var(--ink); text-align: center;
  }
</style>
</head>
<body>
<main class="stage">

  <section class="label front">
    <div class="brand"><span class="dot"></span>Qeshari</div>
    <div class="mascot" role="img" aria-label="Line illustration of a camel head"></div>
    <div class="title-block">
      <p class="title-kicker">Camel</p>
      <h1 class="title">Laban</h1>
      <p class="subtitle">ORGANIC CAMEL BASED MILK</p>
      <p class="note">FENUGREEK ADDED TO ENHANCE FLAVOUR</p>
      <p class="category">FERMENTED MILK</p>
    </div>
    <p class="volume">0,5L</p>
    <p class="fine">Plant based biodegradable bottle (eco-friendly)<br>Shake well before use</p>
  </section>

  <section class="label back">
    <div class="brand">
      <div class="brand-name"><span class="dot"></span>Qeshari</div>
      <div class="brand-line">CAMEL BASED MILK</div>
    </div>
    <p class="story">
      Camel milk is an extremely rich source of proteins with very high antimicrobial and gut protective
      activities — while many of these proteins are not found in cow milk, or found only in minor amounts in cow
      milk. Camel milk has enough nutrients to easily sustain a person through the day as a safe source of
      food, and in many countries camel milk is given to babies suffering from malnutrition.
      A cozy milk with a long flavour, full of benefits.
    </p>
    <div class="nutrition">
      <div class="head">
        <h3>Nutrition<br>Facts</h3>
        <div class="cal"><span>Calories</span><b>245</b></div>
      </div>
      <div class="rows">
        <div class="row"><span>Total Fat</span><span></span></div>
        <div class="row"><span>Sodium</span><span></span></div>
        <div class="row"><span>Total Carbs</span><span></span></div>
        <div class="row"><span>Protein</span><span></span></div>
      </div>
      <div class="side">Percent Daily Values are based on a 2,000 calorie diet.</div>
    </div>
    <p class="fine">Keep refrigerated. Consume within 3 days of opening. Store below 4°C.</p>
  </section>

</main>
</body>
</html>
```